BOLD & MINIMALIST DESIGN NEEDED

We want a very bold but minimalistic business card design that is impactful and utilizes both sides of the business card. Our current logo is included for your use.

We want bold fonts and good use of negative space. We don't want the logo to overpower the design.

Target Market(s)

Professionals who are building new commercial buildings.

Industry/Entity Type

Construction

Contact Information for Business Card

Name, Title, email, office phone, cell phone, website

Font styles to use
Serif
Sans Serif

Requirements
Must have
• Bold design!

```html
<!DOCTYPE html>
<html lang="en">
<head>
<meta charset="utf-8">
<title>Ridgeline Design + Build — Business Card</title>
<link href="https://fonts.googleapis.com/css2?family=Open+Sans:wght@400;700;800&display=swap" rel="stylesheet">
<style>
  :root {
    --backdrop: #242529;
    --paper: #ffffff;
    --green: #84c126;
    --green-deep: #6a9e1f;
    --green-light: #9fd04f;
    --ink: #0c0d0f;
    --grey: #8a8a8a;
  }
  * { box-sizing: border-box; margin: 0; padding: 0; }
  html, body {
    width: 1200px; height: 900px; overflow: hidden;
    background: var(--backdrop);
    font-family: "Open Sans", Arial, sans-serif;
  }
  .canvas {
    position: relative; width: 1200px; height: 900px;
    display: flex; flex-direction: column; align-items: center; justify-content: center; gap: 40px;
  }
  .card {
    position: relative; width: 700px; height: 400px;
    background: var(--paper); overflow: hidden;
    box-shadow: 0 18px 40px rgba(0,0,0,.45);
  }
  .card-art { position: absolute; inset: 0; width: 100%; height: 100%; }

  /* front */
  .front-wordmark {
    position: absolute; left: 300px; right: 30px; top: 0; bottom: 0;
    display: flex; align-items: center; justify-content: center; gap: 14px;
  }
  .brand-square { width: 34px; height: 34px; background: var(--green); flex: none; }
  .brand-name {
    font-weight: 800; color: var(--ink); font-size: 34px; line-height: 1.05;
    letter-spacing: .5px; text-transform: uppercase;
  }

  /* back */
  .back-info {
    position: absolute; left: 400px; right: 30px; top: 60px;
    display: flex; flex-direction: column; align-items: center; text-align: center;
  }
  .back-info .brand { display: flex; align-items: center; gap: 8px; margin-bottom: 26px; }
  .back-info .brand-square { width: 18px; height: 18px; }
  .back-info .brand-name { font-size: 17px; }
  .person-name { font-weight: 700; font-size: 24px; color: var(--ink); }
  .person-title { font-weight: 700; font-size: 17px; color: var(--green); margin-bottom: 30px; }
  .contact-line { font-size: 15px; color: var(--grey); line-height: 1.6; }
</style>
</head>
<body>
<main class="canvas">

  <section class="card card-front">
    <svg class="card-art" viewBox="0 0 700 400" aria-hidden="true">
      <rect x="0" y="0" width="160" height="190" fill="var(--green)"/>
      <rect x="0" y="190" width="175" height="36" fill="var(--ink)"/>
      <rect x="0" y="226" width="175" height="174" fill="var(--green)"/>
      <rect x="175" y="0" width="60" height="400" fill="var(--ink)"/>
      <rect x="160" y="0" width="15" height="190" fill="var(--ink)"/>
    </svg>
    <div class="front-wordmark">
      <span class="brand-square"></span>
      <span class="brand-name">Ridgeline<br>Design + Build</span>
    </div>
  </section>

  <section class="card card-back">
    <svg class="card-art" viewBox="0 0 700 400" aria-hidden="true">
      <polygon points="0,0 40,0 340,145 340,210 0,60" fill="var(--ink)"/>
      <polygon points="0,20 320,190 335,400 0,400" fill="var(--green-deep)"/>
      <polygon points="320,190 345,195 385,230 420,400 330,400" fill="var(--green-light)" opacity=".9"/>
    </svg>
    <div class="back-info">
      <div class="brand">
        <span class="brand-square"></span>
        <span class="brand-name">Ridgeline Design + Build</span>
      </div>
      <p class="person-name">Daniel Marsh</p>
      <p class="person-title">Operations Manager</p>
      <p class="contact-line">daniel.marsh@ridgelinebuild.com</p>
      <p class="contact-line">+000 555 0142 018</p>
    </div>
  </section>

</main>
</body>
</html>
```